Simple POSTER NEEDED by Snow Cone shop, Mobile food vendor

Snow Cone shop / Mobile food vendor needs artist to create a simple colorful graphic 24” x 18” poster for self-serve Snow Cone Flavor Station.
PLEASE SEE DOC "Snow Cone Poster Layout".
Children are the primary customer for our snow cones and the design should be made to appeal to them.
We are featuring 7 popular flavors on the poster. It will be mounted to a flat panel measuring 24” wide by 18” tall with spouts to dispense 7 different flavors.
The main body will be 1 coherent image with sunburst and logo at the top that ties everything together. The bottom 3” or more will be 7 columns of 7 different solid block of color clearly separated. And each with a different color representing that flavor and that spout and each column 2.75” wide.
The hole for each spout is 5/8” and the center of the hole will be 1.5” from the bottom. The spout will partly block the bottom 3.5” of the design.
The separation could be done by means of a solid block of color or by means of a snow cone up.
TEXT & LOGO Easily readable and creative text for each flavor will appear in each column to identify each flavor spout.
COLOR We want the design to look like we could be part of a 1,000 unit fast food franchise, polished and professional not tacky, yet appeal to our primary customer, kids. Perhaps we need to use muted colors or are they called soft or warm colors? Yet bold, bright, and vibrant colors. Please see document “SNOW CONE Poster Layout” to understand what we’re looking for. Please be creative and original. Some type of effect to the background color such as fading or color change might look good. The flavors and colors are: Blue Raspberry (blue) - Lemon Lime (green) - Wild Cherry (red) - Grape (purple) - Orange Pineapple (orange) - Piña Colada (white/slight pinkish/light yellow/creamy yellow) - Banana (yellow) (PLEASE don’t overlook the … ñ.) Rearrange the order of each color/flavor column as you see fit for best design.
IMPORTANT NOTE: The same logo and sunburst that you design for the top portion of the poster will need to be provided for us to print a 28" x 120" sign. PLEASE SEE DOC "Front Cart Signage". This is our logo "Pemvoxa" with a sunburst pattern behind.
We would like to see a variety of border effects around the logo. PLEASE BE CREATIVE AND GIVE US A VARIETY TO CONSIDER!
Thank you, and have fun!

```html
<!DOCTYPE html>
<html lang="en">
<head>
<meta charset="utf-8">
<title>Pemvoxa Snow Cone Flavor Station</title>
<link rel="stylesheet" href="https://fonts.googleapis.com/css2?family=Bangers&display=swap">
<style>
  :root {
    --page-bg: #eef0f3;
    --burst-pink: #e0a9a8;
    --burst-cream: #fbf8ec;
    --logo-red: #e3120b;
    --colada-cup: #e4e3b6;  --colada-ink: #a6a05a;
    --grape-cup: #a240b4;   --grape-ink: #f28ae9;
    --orange-cup: #a79a22;  --orange-ink: #f6e43c;
    --cherry-cup: #b3282c;  --cherry-ink: #ee4650;
    --lime-cup: #3c9c2a;    --lime-ink: #55e23c;
    --rasp-cup: #7840c6;    --rasp-ink: #dba2f2;
    --banana-cup: #c6c63c;  --banana-ink: #f4f25e;
  }
  * { box-sizing: border-box; margin: 0; padding: 0; }
  html, body { width: 1200px; height: 1200px; overflow: hidden; background: var(--page-bg); }
  .poster {
    position: absolute; left: 0; top: 150px;
    width: 1200px; height: 900px; overflow: hidden;
  }
  .sunburst {
    position: absolute; inset: 0;
    background: radial-gradient(ellipse at 66% 52%, var(--burst-cream) 0%, #f3e1dc 45%, var(--burst-pink) 100%);
  }
  .brand {
    position: absolute; left: 0; right: 0; top: 170px;
    text-align: center;
    font-family: "Bangers", system-ui, sans-serif;
    font-size: 150px; letter-spacing: 4px; line-height: 1;
    color: var(--logo-red);
  }
  .flavors {
    position: absolute; left: 130px; right: 0; top: 470px; bottom: 8px;
    display: flex; gap: 4px;
  }
  .flavor {
    flex: 1; position: relative;
    border-radius: 22px 22px 10px 10px;
    display: flex; justify-content: center; align-items: flex-start;
    padding-top: 40px;
  }
  .flavor:first-child { flex: 1.85; justify-content: flex-end; padding-right: 18px; }
  .flavor-name {
    writing-mode: vertical-rl;
    font-family: "Bangers", system-ui, sans-serif;
    font-size: 46px; letter-spacing: 2px; line-height: 1;
  }
  .colada { background: var(--colada-cup); } .colada .flavor-name { color: var(--colada-ink); }
  .grape  { background: var(--grape-cup); }  .grape .flavor-name  { color: var(--grape-ink); font-size: 64px; }
  .orange { background: var(--orange-cup); } .orange .flavor-name { color: var(--orange-ink); }
  .cherry { background: var(--cherry-cup); } .cherry .flavor-name { color: var(--cherry-ink); }
  .lime   { background: var(--lime-cup); }   .lime .flavor-name   { color: var(--lime-ink); }
  .rasp   { background: var(--rasp-cup); }   .rasp .flavor-name   { color: var(--rasp-ink); }
  .banana { background: var(--banana-cup); } .banana .flavor-name { color: var(--banana-ink); font-size: 64px; }
</style>
</head>
<body>
  <main class="poster">
    <div class="sunburst" role="img" aria-label="Pink and cream sunburst rays radiating from behind the logo"></div>
    <h1 class="brand">Pemvoxa</h1>
    <section class="flavors">
      <div class="flavor colada" role="img" aria-label="Piña colada snow cone cup with red straw"><span class="flavor-name">Piña Colada</span></div>
      <div class="flavor grape" role="img" aria-label="Grape snow cone cup with red straw"><span class="flavor-name">Grape</span></div>
      <div class="flavor orange" role="img" aria-label="Orange pineapple snow cone cup with red straw"><span class="flavor-name">Orange Pineapple</span></div>
      <div class="flavor cherry" role="img" aria-label="Wild cherry snow cone cup with red straw"><span class="flavor-name">Wild Cherry</span></div>
      <div class="flavor lime" role="img" aria-label="Lemon lime snow cone cup with red straw"><span class="flavor-name">Lemon Lime</span></div>
      <div class="flavor rasp" role="img" aria-label="Blue raspberry snow cone cup with red straw"><span class="flavor-name">Blue Raspberry</span></div>
      <div class="flavor banana" role="img" aria-label="Banana snow cone cup with red straw"><span class="flavor-name">Banana</span></div>
    </section>
  </main>
</body>
</html>
```